Norvale Chem Business Card Design

We are looking to make our business cards consistent and modernize them. They are very boring and want to add color.
The final design should communicate a business feel and we are focused on our customer.

Industry/Entity Type

Business

Contact Information for Business Card

Norvale Chem Corporation
812 W. Larkspur Avenue
Suite 342
Itasca, IL 60198
Dana Pellowski
Marketing Manager
dpellowski@norvalechem-example.com
630-555-0184
Your Trusted Partner in Specialty Chemical Supply

Requirements
Must have
• 400 lb stock
Common font
Both sides but don't fill whole back side
Nice to have
• Metallic finish, raised print or spot gloss
Should not have
• cheap paper

```html
<!DOCTYPE html>
<html lang="en">
<head>
<meta charset="utf-8">
<title>Norvale Chem Business Card Design</title>
<link rel="stylesheet" href="https://fonts.googleapis.com/css2?family=Signika:wght@300;400&display=swap">
<style>
  :root {
    --bg: #e9ecea;
    --paper: #ffffff;
    --mint: #a9dccb;
    --teal: #5cc2a6;
    --green: #3f9a7f;
    --green-deep: #1f6b50;
    --brand: #0e6a45;
    --ink: #1d4f3e;
  }
  * { box-sizing: border-box; margin: 0; padding: 0; }
  html, body {
    width: 1200px; height: 1000px; overflow: hidden;
    background: var(--bg);
    font-family: "Signika", sans-serif;
  }
  .sheet {
    width: 1200px; height: 1000px;
    display: flex; flex-direction: column;
    align-items: center; justify-content: center; gap: 60px;
  }
  .card {
    position: relative;
    width: 700px; height: 400px;
    border-radius: 4px; overflow: hidden;
    background: var(--paper);
    box-shadow: 0 6px 18px rgba(0,0,0,.14);
  }
  .card-art { position: absolute; inset: 0; width: 100%; height: 100%; }
  .wordmark {
    position: absolute;
    display: flex; align-items: center; gap: 12px;
    color: var(--brand); font-weight: 400;
    white-space: nowrap;
  }
  .wordmark-square { background: var(--brand); flex: none; }
  .card--back .wordmark { top: 70px; right: 60px; font-size: 20px; }
  .card--back .wordmark-square { width: 26px; height: 26px; }
  .card--front .wordmark { top: 160px; right: 60px; font-size: 24px; }
  .card--front .wordmark-square { width: 36px; height: 36px; }
  .contact {
    position: absolute; left: 40px; top: 150px;
    color: var(--ink); font-weight: 300; font-size: 17px; line-height: 1.4;
  }
  .contact .person { margin-top: 10px; }
  .tagline {
    position: absolute; left: 40px; bottom: 26px;
    color: #fff; font-weight: 300; font-size: 21px; letter-spacing: .2px;
    white-space: nowrap;
  }
</style>
</head>
<body>
<main class="sheet">

  <section class="card card--back" aria-label="Card back with contact details">
    <svg class="card-art" viewBox="0 0 700 400" aria-hidden="true">
      <defs>
        <linearGradient id="backPaper" x1="0" y1="1" x2="1" y2="0">
          <stop offset="0" stop-color="#bfe5d7"/>
          <stop offset="0.6" stop-color="#f3faf7"/>
          <stop offset="1" stop-color="#ffffff"/>
        </linearGradient>
      </defs>
      <rect width="700" height="400" fill="var(--green)"/>
      <path d="M170 0 C 270 70, 330 190, 480 225 C 580 248, 650 250, 700 250 L700 0 Z" fill="var(--green-deep)"/>
      <path d="M215 0 C 300 60, 360 175, 500 205 C 590 224, 650 228, 700 228 L700 0 Z" fill="url(#backPaper)"/>
      <path d="M470 400 C 500 330, 600 310, 700 322 L700 400 Z" fill="var(--teal)"/>
    </svg>
    <div class="wordmark"><span class="wordmark-square"></span>Norvale Chem Corporation</div>
    <div class="contact">
      <p>Norvale Chem Corporation</p>
      <p>812 W. Larkspur Avenue Suite 342 Maple Ridge</p>
      <p>OH 60198</p>
      <p class="person">Dana Pellowski</p>
      <p>Marketing Manager</p>
      <p>dpellowski@norvalechem-example.com</p>
      <p>630-555-0184</p>
    </div>
    <p class="tagline">Your Trusted Partner in Specialty Chemical Supply</p>
  </section>

  <section class="card card--front" aria-label="Card front with company name">
    <svg class="card-art" viewBox="0 0 700 400" aria-hidden="true">
      <defs>
        <linearGradient id="frontPaper" x1="0" y1="0" x2="1" y2="1">
          <stop offset="0" stop-color="#cfeae0"/>
          <stop offset="0.55" stop-color="#f5fbf8"/>
          <stop offset="1" stop-color="#ffffff"/>
        </linearGradient>
      </defs>
      <rect width="700" height="400" fill="url(#frontPaper)"/>
      <path d="M0 0 L110 0 C 170 130, 280 290, 470 335 C 570 358, 650 362, 700 362 L700 400 L0 400 Z" fill="var(--green)"/>
      <path d="M60 0 L110 0 C 170 130, 280 290, 470 335 C 570 358, 650 362, 700 362 L700 378 C 600 378, 480 368, 400 340 C 250 290, 130 150, 60 0 Z" fill="var(--green-deep)"/>
      <path d="M0 0 L60 0 C 120 150, 200 280, 330 360 C 360 378, 390 392, 420 400 L0 400 Z" fill="var(--mint)" opacity=".55"/>
    </svg>
    <div class="wordmark"><span class="wordmark-square"></span>Norvale Chem Corporation</div>
  </section>

</main>
</body>
</html>
```